Flyer-Design für verschiedene Anwendungsfälle bzw. Produkte
Zielgruppe
Wir lösen reale Probleme mit digitalen Technologien wie IoT und KI. In unseren Projekten liefern wir Gesamtlösungen von der Strategieberatung über Konzepterstellung bis zur technischen Umsetzung und dem Betrieb. Integration und Konzeption spielen eine große Rolle, wir sind kein Hardwareanbieter, sondern bauen Komplettlösungen aus Software, Connectivity und Hardware. Unsere Kunden sind gehobener Mittelstand bis Konzern, ab 25 Mio € aufwärts. Oft sind unsere Kunden aus konservativen Branchen. Wir müssen beim Design immer einen Kompromiss aus innovativ und Vertrauen erweckend finden. Unsere Persona ist weiß, männlich, über 50, nicht besonders technologieaffin.
Aufgabenstellung
Wir brauchen eine Flyer-Vorlage für verschiedene Anwendungsfälle bzw. Produkte. Im Anhang sind Beispiele für Produktbeschreibungen, sowie ein Flyer, den wir selbst designet haben.
Ergebnis soll ein Flyer-Design sein, das wir für solche Produkte immer wieder verwenden können, DIN A5 zweiseitig.
Exo2 und Trebuchet sind unsere Schriftarten. Logos habe ich in 2 Formaten angehängt.
Website: tavolu.me
Wenn Sie weitere Ideen haben, sind wir ganz Ohr.
Grafisch bitte nur die Farben grau, schwarz und orange verwenden (grau und orange siehe Logo)

```html
<!DOCTYPE html>
<html lang="de">
<head>
<meta charset="utf-8">
<title>Smart City – Glättemeldesystem Flyer</title>
<link href="https://fonts.googleapis.com/css2?family=Exo+2:wght@300;400;500;600;700;800&display=swap" rel="stylesheet">
<style>
:root{
  --orange-deep:#d6481a;
  --orange:#e2701f;
  --orange-light:#eaa233;
  --ink:#1b1b1b;
  --text:#2e2e2e;
  --grey-light:#ededed;
  --grey-mid:#dcdcdc;
  --stage:#d5d6da;
  --photo-a:#c9ccd1;
  --photo-b:#f3f3f3;
}
*{margin:0;padding:0;box-sizing:border-box}
html,body{width:1200px;height:800px;overflow:hidden}
body{background:var(--stage);font-family:"Exo 2",sans-serif;color:var(--text);position:relative}
.flyer{position:absolute;top:104px;width:424px;height:598px;background:var(--grey-light);overflow:hidden;box-shadow:0 6px 18px rgba(0,0,0,.18)}
.flyer--front{left:138px}
.flyer--back{left:634px}
.abs{position:absolute}
.grad{background:linear-gradient(90deg,var(--orange-deep),var(--orange) 45%,var(--orange-light))}
.photo{position:absolute;background:linear-gradient(135deg,var(--photo-a),var(--photo-b) 60%,#e8e3dc)}

/* front */
.brand{left:28px;top:50px;font-size:22px;font-weight:600;letter-spacing:5px;color:var(--orange)}
.front-photo{left:150px;top:73px;width:274px;height:207px;clip-path:polygon(0 0,100% 0,100% 100%,45% 100%,0 0);background:linear-gradient(120deg,#b8bcc2,#eef0f2 55%,#f7f7f7)}
.front-accent{left:280px;top:34px;width:144px;height:67px;clip-path:polygon(20% 0,100% 0,100% 100%,62% 100%,0 75%)}
.title-band{left:0;top:111px;width:250px;height:157px;clip-path:polygon(0 0,69% 0,99% 84%,66% 84%,61% 100%,0 100%)}
.title{left:28px;top:124px;font-size:37px;line-height:36px;font-weight:800;color:var(--ink)}
.subtitle{left:28px;top:208px;font-size:18px;line-height:19px;font-weight:600;color:var(--ink)}
.benefit-col{left:221px;top:280px;width:203px;height:257px;background:linear-gradient(180deg,#e6e6e6,#d8d8d8 70%,#e2e2e2)}
.lead{font-size:20px;font-weight:300;line-height:23px;color:#3a3a3a}
.lead strong{display:block;font-weight:700;color:var(--orange)}
.task{left:28px;top:305px;width:180px}
.solution{left:246px;top:305px;width:170px}
.body{font-size:11px;line-height:13.4px;font-weight:400}
.body p+p{margin-top:7px}
.task-text{left:28px;top:368px;width:180px}
.benefits{left:246px;top:368px;width:170px;list-style:none}
.benefits li{position:relative;padding-left:20px;margin-bottom:8px}
.benefits svg{position:absolute;left:0;top:1px}
.front-strip{left:0;top:530px;width:111px;height:8px;clip-path:polygon(0 0,100% 0,94% 100%,0 100%)}
.footer{left:0;width:100%;font-weight:600;color:var(--ink)}
.front-footer{top:537px;height:61px;padding:13px 0 0 28px;font-size:11px}
.contacts{display:flex;gap:16px;align-items:center;margin-top:9px}
.contacts span{display:flex;align-items:center;gap:5px}

/* back */
.back-photo{left:154px;top:0;width:270px;height:194px;clip-path:polygon(0 0,100% 0,100% 100%,18% 100%);background:linear-gradient(160deg,#c7d0dc,#9ea9b6 50%,#56595e)}
.pilot-band{left:0;top:18px;width:260px;height:154px;clip-path:polygon(0 0,81% 0,100% 100%,0 100%)}
.pilot-title{left:26px;top:43px;font-size:21px;line-height:25px;font-weight:800;color:var(--ink)}
.pilot-list{left:26px;top:104px;font-size:12px;line-height:15px;font-weight:600;color:var(--ink);list-style:none}
.pilot-list li::before{content:"· "}
.info{top:194px;left:0;width:100%;height:153px;background:#f1f1f1}
.info-col{top:214px;width:118px;border-left:1px solid var(--orange);padding-left:6px;height:112px}
.info-col h3{font-size:13px;font-weight:700;color:var(--orange);margin-bottom:10px}
.info-col p{font-size:8.6px;line-height:11px}
.info-col p+p{margin-top:4px}
.info-end{left:404px;top:214px;height:112px;border-left:1px solid var(--orange)}
.offer{top:347px;left:0;width:100%;height:140px;background:linear-gradient(90deg,#e6e6e6,#dadada)}
.offer-title{top:374px;left:0;width:424px;text-align:center;font-size:19px;font-weight:700;color:var(--orange)}
.badge{left:337px;top:341px;width:72px;height:72px;border-radius:50%;display:flex;align-items:center;justify-content:center;text-align:center;font-size:8px;line-height:10px;font-weight:700;color:var(--ink);transform:rotate(6deg)}
.offer-row{left:0;width:424px;font-size:10.5px;font-weight:600;color:var(--ink)}
.offer-row .l{position:absolute;right:245px;white-space:nowrap}
.offer-row .r{position:absolute;left:236px;white-space:nowrap}
.offer-row svg{position:absolute;top:0}
.back-strip{left:310px;top:487px;width:114px;height:9px;clip-path:polygon(0 0,100% 0,100% 100%,4% 100%)}
.back-footer{top:496px;height:102px;padding:20px 0 0 28px;font-size:11.5px;line-height:15px}
.back-footer .contacts{margin-top:9px;font-size:11px}
</style>
</head>
<body>

<svg width="0" height="0" style="position:absolute">
  <defs>
    <symbol id="tick" viewBox="0 0 14 14"><circle cx="7" cy="7" r="6" fill="none" stroke="#e2701f" stroke-width="1.2"/><path d="M4 7.2l2 2 4-4.2" fill="none" stroke="#e2701f" stroke-width="1.3"/></symbol>
    <symbol id="phone" viewBox="0 0 12 12"><path d="M3 1l2 2.5-1.2 1.2a7 7 0 0 0 3.5 3.5L8.5 7 11 9l-1.5 1.8C5.5 10.5 1.5 6.5 1.2 2.5z" fill="none" stroke="#1b1b1b" stroke-width="1"/></symbol>
    <symbol id="mail" viewBox="0 0 12 12"><rect x="1" y="2.5" width="10" height="7" fill="none" stroke="#1b1b1b" stroke-width="1"/><path d="M1 2.5l5 4 5-4" fill="none" stroke="#1b1b1b" stroke-width="1"/></symbol>
    <symbol id="globe" viewBox="0 0 12 12"><circle cx="6" cy="6" r="5" fill="none" stroke="#1b1b1b" stroke-width="1"/><ellipse cx="6" cy="6" rx="2.2" ry="5" fill="none" stroke="#1b1b1b" stroke-width=".9"/><path d="M1 6h10M2 3.5h8M2 8.5h8" stroke="#1b1b1b" stroke-width=".8"/></symbol>
  </defs>
</svg>

<!-- Vorderseite -->
<section class="flyer flyer--front">
  <div class="abs brand">TAVOLU</div>
  <div class="photo front-photo" role="img" aria-label="Foto: Winterdienst-Streufahrzeug auf verschneiter Stadtstraße"></div>
  <div class="abs grad front-accent"></div>
  <div class="abs grad title-band"></div>
  <h1 class="abs title">SMART<br>CITY</h1>
  <div class="abs subtitle">Glättemeldesystem<br>per Funk</div>

  <div class="abs benefit-col"></div>

  <h2 class="abs lead task">Ihre Aufgabe -<strong>Ein Problem?</strong></h2>
  <div class="abs body task-text">
    <p>Ist die Erfüllung ihrer hoheitlichen Aufgabe der Räum- und Streu&shy;pflicht schlwer planbar und aufwendig?</p>
    <p><strong style="font-weight:600;color:var(--ink)">Das muss nicht sein!</strong></p>
    <p>Die regelmäßige Übertragung an das Umweltamt können Sie jetzt auch mit unserer IoT Lösung digitalisieren.</p>
  </div>

  <h2 class="abs lead solution">Unsere Lösung -<strong>Ihre Vorteile</strong></h2>
  <ul class="abs body benefits">
    <li><svg width="13" height="13"><use href="#tick"/></svg>Präzise und sofortige Warnung, wenn ein Ort von Eis- oder Schneeglätte betroffen ist</li>
    <li><svg width="13" height="13"><use href="#tick"/></svg>Schnelle Reaktion durch Winterdienst möglich</li>
    <li><svg width="13" height="13"><use href="#tick"/></svg>Frühzeitige Warnung und Winterdienst können zu einer deutlichen Steige&shy;rung der Sicherheit führen</li>
  </ul>

  <div class="abs grad front-strip"></div>
  <footer class="abs grad footer front-footer">
    <div>Kontakt:</div>
    <div class="contacts">
      <span><svg width="11" height="11"><use href="#phone"/></svg>+49(0)1579204836</span>
      <span><svg width="11" height="11"><use href="#mail"/></svg>iot@tavolu.me</span>
      <span><svg width="11" height="11"><use href="#globe"/></svg>www.tavolu.me</span>
    </div>
  </footer>
</section>

<!-- Rückseite -->
<section class="flyer flyer--back">
  <div class="photo back-photo" role="img" aria-label="Foto: berührungsloser Straßensensor an einem Mast"></div>
  <div class="abs grad pilot-band"></div>
  <h2 class="abs pilot-title">Pilotprojekt<br>ab 4.999€</h2>
  <ul class="abs pilot-list">
    <li>Abdeckung von 3 Messstellen</li>
    <li>Datenvisualisierung</li>
    <li>3 Monate Betrieb inklusive</li>
  </ul>

  <div class="abs info"></div>
  <div class="abs info-col" style="left:18px">
    <h3>Funktionsweise</h3>
    <p>Ein Sensor erhebt kontinu&shy;ierlich alle Informationen, die nötig sind um festzu&shy;stellen, ob ein Punkt (Straße, Schiene, Lande&shy;bahn etc.) von Eis- oder Schneeglätte betroffen ist</p>
  </div>
  <div class="abs info-col" style="left:146px">
    <h3>Hardware</h3>
    <p>Berührungsloser Straßen&shy;sensor mit LoRaWAN oder NB IoT Übertragungsmodul.</p>
    <p>Die Kombination mit einer Wetterstation ermöglicht bessere und frühere Voraussagen.</p>
  </div>
  <div class="abs info-col" style="left:274px">
    <h3>Frontend</h3>
    <p>Alle Daten werden in einem Dashboard geographisch und als Heatmap angezeigt. Bei Über- oder Unterschrei&shy;tung bestimmter Werte werden per Mail oder SMS Meldungen verschickt.</p>
  </div>
  <div class="abs info-end"></div>

  <div class="abs offer"></div>
  <h2 class="abs offer-title">Unser Angebot</h2>
  <div class="abs grad badge">Anbindung<br>an Leitsysteme<br>möglich</div>

  <div class="abs offer-row" style="top:418px">
    <span class="l">Konzeption</span>
    <svg width="12" height="12" style="left:188px"><use href="#tick"/></svg>
    <svg width="12" height="12" style="left:213px"><use href="#tick"/></svg>
    <span class="r">Funktionalitätstest</span>
  </div>
  <div class="abs offer-row" style="top:437px">
    <span class="l">Hardwareauswahl</span>
    <svg width="12" height="12" style="left:188px"><use href="#tick"/></svg>
    <svg width="12" height="12" style="left:213px"><use href="#tick"/></svg>
    <span class="r">Visualisierung</span>
  </div>
  <div class="abs offer-row" style="top:457px">
    <span class="l">Konfiguration und Einrichtung</span>
    <svg width="12" height="12" style="left:188px"><use href="#tick"/></svg>
    <svg width="12" height="12" style="left:213px"><use href="#tick"/></svg>
    <span class="r">Betrieb</span>
  </div>

  <div class="abs grad back-strip"></div>
  <footer class="abs grad footer back-footer">
    <div>Für Ihr Pilotprojekt und andere IoT Anwendungen im Bereich<br>Smart City erreichen Sie uns hier:</div>
    <div class="contacts">
      <span><svg width="11" height="11"><use href="#phone"/></svg>+49(0)1579204836</span>
      <span><svg width="11" height="11"><use href="#mail"/></svg>iot@tavolu.me</span>
      <span><svg width="11" height="11"><use href="#globe"/></svg>www.tavolu.me</span>
    </div>
  </footer>
</section>

</body>
</html>
```